Request for Business Card Design

Hi. My name is Marlena, I am looking for a new business card design for my company, Quillbrook Sensing Systems, LLC. I really like the design you did for Tavel Harvest and was hoping you could do something similar using our full logo and our mark. I am also open to any raised texture design using our mark. I have attached our full logo, which would need to be somewhere on the card, as well as the mark in both outline and full form, as well as our brand colors / guide. The card does not have to be white, as long as our logo and mark appear. I actually like darker colored business cards more, but am open to all options. If you are interested in working with me, please let me know. We would also take the business card design into letterhead design if you can do that.

```html
<!DOCTYPE html>
<html lang="en">
<head>
<meta charset="utf-8">
<title>Quillbrook Sensing Systems – Business Card</title>
<link href="https://fonts.googleapis.com/css2?family=Montserrat:wght@400;600;700&display=swap" rel="stylesheet">
<style>
  :root{
    --canvas:#2b2826;
    --card:#1b1b1c;
    --card-back:#0e0e0f;
    --brand-blue:#1d9bc9;
    --text-light:#f2f2f2;
    --text-muted:#bdbdbd;
    --divider:#1d9bc9;
  }
  *{margin:0;padding:0;box-sizing:border-box}
  html,body{width:1200px;height:786px;overflow:hidden;background:var(--canvas)}
  body{font-family:"Montserrat",sans-serif;position:relative}
  .card{position:absolute;top:245px;width:520px;height:297px;border-radius:3px;box-shadow:0 10px 30px rgba(0,0,0,.45);overflow:hidden}
  .card--front{left:50px;background:var(--card)}
  .card--back{left:630px;background:var(--card-back)}

  .brand{position:absolute;display:flex;align-items:center;gap:10px}
  .brand__dot{width:30px;height:30px;border-radius:50%;background:var(--brand-blue);flex:none}
  .brand__name{color:var(--text-light);font-weight:600;line-height:1.05;text-transform:uppercase;white-space:nowrap}
  .brand__name .line1{display:block;font-size:20px;letter-spacing:1.5px}
  .brand__name .line2{display:block;font-size:7.5px;letter-spacing:1px;margin-top:3px}
  .card--front .brand{left:30px;top:186px}

  .divider{position:absolute;left:272px;top:88px;width:1.5px;height:120px;background:var(--divider)}

  .contact{position:absolute;left:292px;top:84px;color:var(--text-light)}
  .contact__name{font-size:19px;font-weight:700;color:var(--brand-blue);white-space:nowrap}
  .contact__role{font-size:11px;color:var(--text-muted);margin-bottom:6px}
  .contact__row{display:flex;align-items:center;gap:8px;font-size:11px;line-height:17px;white-space:nowrap}
  .contact__row svg{width:10px;height:10px;fill:var(--brand-blue);flex:none}
  .contact__address{font-size:11px;line-height:15px;margin-top:9px;padding-left:18px;white-space:nowrap}

  .pattern{position:absolute;inset:0;background:
    radial-gradient(ellipse at 8% 20%,rgba(170,170,172,.55) 0%,rgba(90,90,92,.25) 30%,transparent 60%),
    linear-gradient(115deg,#4a4a4c 0%,#262628 35%,#141415 70%,#0c0c0d 100%)}
  .card--back .brand{right:26px;top:122px;background:rgba(14,14,15,.85);padding:8px 10px;border-radius:2px}
  .card--back .brand__name .line1{font-size:20px}
  .card--back .brand__name .line2{font-size:7.5px}
  .card--back .brand__dot{width:28px;height:28px}
</style>
</head>
<body>

<section class="card card--front" aria-label="Card front">
  <div class="brand">
    <span class="brand__dot"></span>
    <span class="brand__name"><span class="line1">Quillbrook</span><span class="line2">Sensing Systems</span></span>
  </div>
  <div class="divider"></div>
  <div class="contact">
    <p class="contact__name">Marlena Ostrand</p>
    <p class="contact__role">Owner</p>
    <p class="contact__row">
      <svg viewBox="0 0 10 10"><path d="M2 0.5 3.6 2.6 2.7 3.6C3.3 5 4.9 6.6 6.3 7.3L7.4 6.4 9.5 8 8.6 9.4C4.5 9 1 5.5.6 1.4Z"/></svg>
      +001 303 555 0142
    </p>
    <p class="contact__row">
      <svg viewBox="0 0 10 10"><path d="M0 2h10v6H0Zm.8.6L5 5.6 9.2 2.6Z"/></svg>
      info@quillbrooksensing.com
    </p>
    <p class="contact__row">
      <svg viewBox="0 0 10 10"><circle cx="5" cy="5" r="4.5"/></svg>
      www.quillbrooksensing.com
    </p>
    <p class="contact__address">1180 Harbor Ridge Lane<br>Fairvale, CO 80000</p>
  </div>
</section>

<section class="card card--back" aria-label="Card back">
  <div class="pattern" role="img" aria-label="Raised gloss pattern of the brand mark repeated across the card"></div>
  <div class="brand">
    <span class="brand__dot"></span>
    <span class="brand__name"><span class="line1">Quillbrook</span><span class="line2">Sensing Systems</span></span>
  </div>
</section>

</body>
</html>
```